Website Landing Page for Brightfall Systems

Create a custom designed website landing page for our business. Looking for a professional upscale design that incorporates our logo and logo colors into the theme. I want a standard fixed frame website, not a constant scrolling format that seems to be the trend. To start with I'm looking for more of the graphic design part, maybe a concept or theme, I don't expect to see a finished project. Not interested in generic templates or layouts.

The name of our company is Brightfall Systems and I've attached our logo below. I'd like to have the web page have the same look and feel of our logo, as well as the colors. Our company, Brightfall Systems does system design, installation, and programming, of residential and commercial Audio/Video and Automation systems. We do home theaters, lighting and building automation, video conferencing systems, security camera installations, conference rooms, projectors, distributed audio systems, and similar Technology projects. This will be a professional services/informational website. We will not sell products on this website. This website will be used to advertise our company and communicate our services to prospective customers. Having a well designed, professional and clean website is one way we want to distinguish our company from the competition.

Here are some examples of what I consider a professional well designed website
http://www.qorlamstudio.com/Work/

Last year we had our tradlo store designed (with PixelMarket) and I'm really happy with the way it turned out. You can see it at www.HolvenGearDepot.com I consider this to be a great design and looking for the same level of quality with this new website. However, do not copy or use any part of this design in this new project. This tradlo store is completely separate from our other company Brightfall Systems. I only mention this tradlo store an an example of good work.

Reason: Still going through designs.

Reason: Still working on project and have not had time to review all designs and request revisions.

Reason: Sill going through designs and requesting revisions

Reason: still going through all the submissions we received.

Target Market(s)

People interested in Audio/Video, home theaters, home automation. We do sales, system design, and programming. We typically work on larger projects with both residential and commercial customers.

Industry/Entity Type

Business

Number of Pages Required

1 page

Requirements
Must have
• Great design elements. Please use a white background. I think white goes well with our logo colors.

```html
<!DOCTYPE html>
<html lang="en">
<head>
<meta charset="utf-8">
<title>Brightfall Systems</title>
<link href="https://fonts.googleapis.com/css2?family=Oswald:wght@400;500&family=Open+Sans:wght@400&family=Lato:wght@400&display=swap" rel="stylesheet">
<style>
  :root{
    --blue:#3a7cc8;
    --green:#6abf45;
    --ink:#2b2b2b;
    --text:#333;
    --white:#fff;
    --hero-dark:#2d2a28;
  }
  *{margin:0;padding:0;box-sizing:border-box}
  html,body{width:1094px;height:1200px;overflow:hidden;background:var(--white)}
  body{position:relative;font-family:"Open Sans",sans-serif;color:var(--text)}
  .abs{position:absolute}

  .hero-photo{left:0;top:0;width:1094px;height:504px;
    background:radial-gradient(ellipse at 50% 40%,#5a4a40 0%,#3b332e 45%,#1f1d1c 100%),linear-gradient(#4a4a4a,#222)}
  .hero-shade{left:0;top:0;width:1094px;height:504px;
    background:linear-gradient(90deg,rgba(80,80,80,.35),rgba(0,0,0,0) 40%,rgba(0,0,0,0) 70%,rgba(90,90,90,.3)),
               linear-gradient(180deg,rgba(0,0,0,0) 60%,rgba(20,20,22,.5))}

  .brand-small{left:70px;top:26px;display:flex;flex-direction:column;align-items:center;gap:5px}
  .brand-small .dot{width:28px;height:28px;border-radius:50%;border:3px solid var(--blue)}
  .brand-small .name{font-family:"Oswald",sans-serif;font-size:9px;letter-spacing:.5px;color:var(--blue)}

  .nav{top:46px;font-family:"Oswald",sans-serif;font-size:12px;color:var(--white)}
  .nav-about{left:780px}.nav-services{left:849px}.nav-contact{left:927px}
  .nav-search{left:1012px;top:47px}

  .headline{left:104px;top:146px;font-family:"Oswald",sans-serif;font-weight:400;font-size:68px;line-height:70px;color:var(--white);letter-spacing:-1px}
  .headline .blue{color:var(--blue)}
  .headline .green{color:var(--green)}
  .hero-rule{left:106px;top:297px;width:50px;height:2px;background:var(--blue)}
  .hero-lede{left:108px;top:309px;font-family:"Lato",sans-serif;font-size:16px;line-height:19px;color:var(--white)}
  .scroll-cue{left:524px;top:442px}

  .section-title{font-family:"Oswald",sans-serif;font-weight:400;font-size:50px;line-height:56px;color:var(--ink);letter-spacing:-.5px}
  .section-rule{width:50px;height:3px;background:var(--ink)}
  .section-text{font-size:13px;line-height:19px;color:var(--text)}
  .outline-btn{width:155px;height:38px;border:2px solid var(--ink);display:flex;align-items:center;justify-content:center;
    font-size:11.5px;letter-spacing:.4px;color:var(--ink)}

  .about-title{left:160px;top:560px}
  .about-rule{left:160px;top:633px}
  .about-text{left:158px;top:649px;width:300px}
  .about-btn{left:158px;top:705px}

  .brand-large{left:656px;top:550px;width:200px;display:flex;flex-direction:column;align-items:center;gap:14px}
  .brand-large .dot{width:112px;height:112px;border-radius:50%;border:6px solid var(--blue)}
  .brand-large .name{font-family:"Oswald",sans-serif;font-weight:500;font-size:31px;line-height:35px;text-align:center;color:var(--blue);letter-spacing:1px}

  .services-title{left:160px;top:866px}
  .services-rule{left:160px;top:939px}
  .services-text{left:158px;top:953px;width:360px;font-size:15px;line-height:19px}
  .services-btn{left:158px;top:1000px;height:42px}

  .service{width:200px;display:flex;flex-direction:column;align-items:center;text-align:center;
    font-size:12.5px;line-height:19px;letter-spacing:.3px;color:var(--ink)}
  .svc-auto{left:576px;top:842px}
  .svc-prog{left:787px;top:842px}
  .svc-theater{left:574px;top:970px}
  .svc-camera{left:791px;top:964px}
  .service svg{margin-bottom:12px}

  .footer{left:0;top:1145px;width:1094px;height:55px;background:var(--green);display:flex;align-items:center;padding-left:78px;
    font-size:12px;color:var(--white)}
  .footer a{color:var(--white);text-decoration:underline}
</style>
</head>
<body>
  <div class="abs hero-photo" role="img" aria-label="Photo of a modern conference room with a long table, black chairs, wood-panelled wall and wall-mounted display"></div>
  <div class="abs hero-shade"></div>

  <div class="abs brand-small"><span class="dot"></span><span class="name">BRIGHTFALL SYSTEMS</span></div>

  <a class="abs nav nav-about">About Us</a>
  <a class="abs nav nav-services">Services</a>
  <a class="abs nav nav-contact">Contact Us</a>
  <svg class="abs nav-search" width="12" height="12" viewBox="0 0 12 12" aria-label="Search"><circle cx="5" cy="5" r="3.8" fill="none" stroke="#fff" stroke-width="1.4"/><line x1="7.8" y1="7.8" x2="11" y2="11" stroke="#fff" stroke-width="1.4"/></svg>

  <h1 class="abs headline"><span class="blue">LESS</span> DOWNTIME,<br><span class="green">MORE</span> PRODUCTIVITY</h1>
  <div class="abs hero-rule"></div>
  <p class="abs hero-lede">Lorem ipsum dolor sit amet, consectetur adipiscing elit.<br>Nulla fringilla diam sem</p>
  <svg class="abs scroll-cue" width="58" height="38" viewBox="0 0 58 38" aria-label="Scroll down"><polyline points="7,7 29,29 51,7" fill="none" stroke="#1c1c1c" stroke-width="11" stroke-linecap="round" stroke-linejoin="round"/></svg>

  <h2 class="abs section-title about-title">ABOUT US</h2>
  <div class="abs section-rule about-rule"></div>
  <p class="abs section-text about-text">Lorem ipsum dolor sit amet, consectetur adipiscing elit. Nulla fringilla diam sem, iaculis</p>
  <a class="abs outline-btn about-btn">LEARN MORE</a>

  <div class="abs brand-large"><span class="dot"></span><span class="name">BRIGHTFALL<br>SYSTEMS</span></div>

  <h2 class="abs section-title services-title">SERVICES</h2>
  <div class="abs section-rule services-rule"></div>
  <p class="abs section-text services-text">Lorem ipsum dolor sit amet, consectetur adipiscing elit. Nulla fringilla diam sem,</p>
  <a class="abs outline-btn services-btn">SEE MORE</a>

  <div class="abs service svc-auto">
    <svg width="54" height="56" viewBox="0 0 54 56" aria-hidden="true">
      <path d="M10 8 C22 -2 40 6 44 18 L50 34 C54 46 44 54 34 50 L14 40 C2 34 0 16 10 8Z" fill="none" stroke="var(--blue)" stroke-width="3"/>
      <g fill="var(--blue)"><circle cx="22" cy="22" r="9"/>
      <g stroke="var(--blue)" stroke-width="5"><line x1="22" y1="8" x2="22" y2="36"/><line x1="8" y1="22" x2="36" y2="22"/><line x1="12" y1="12" x2="32" y2="32"/><line x1="32" y1="12" x2="12" y2="32"/></g></g>
      <circle cx="22" cy="22" r="4" fill="#fff"/>
      <circle cx="40" cy="42" r="6" fill="var(--blue)"/>
    </svg>
    AUTOMATION SYSTEMS
  </div>

  <div class="abs service svc-prog">
    <svg width="50" height="46" viewBox="0 0 50 46" aria-hidden="true">
      <rect x="1.5" y="1.5" width="47" height="43" fill="none" stroke="var(--blue)" stroke-width="3"/>
      <rect x="1.5" y="1.5" width="47" height="8" fill="var(--blue)"/>
      <g fill="#fff"><circle cx="35" cy="5.5" r="1.4"/><circle cx="39.5" cy="5.5" r="1.4"/><circle cx="44" cy="5.5" r="1.4"/></g>
      <g fill="none" stroke="var(--blue)" stroke-width="3" stroke-linecap="round" stroke-linejoin="round"><polyline points="18,20 11,26 18,32"/><polyline points="32,20 39,26 32,32"/><line x1="28" y1="18" x2="22" y2="34"/></g>
    </svg>
    PROGRAMMING
  </div>

  <div class="abs service svc-theater">
    <svg width="70" height="54" viewBox="0 0 70 54" aria-hidden="true">
      <g fill="none" stroke="var(--blue)" stroke-width="2.4">
        <rect x="10" y="2" width="50" height="7"/>
        <rect x="24" y="16" width="22" height="16"/>
        <rect x="10" y="18" width="9" height="18"/><rect x="51" y="18" width="9" height="18"/>
        <rect x="2" y="40" width="66" height="8"/>
        <line x1="6" y1="48" x2="6" y2="53"/><line x1="64" y1="48" x2="64" y2="53"/>
      </g>
      <g fill="var(--blue)"><circle cx="16" cy="5.5" r="1.6"/><circle cx="22" cy="5.5" r="1.6"/><circle cx="48" cy="5.5" r="1.6"/><circle cx="54" cy="5.5" r="1.6"/>
      <rect x="33" y="32" width="4" height="6"/><circle cx="14.5" cy="30" r="2.2"/><circle cx="55.5" cy="30" r="2.2"/><rect x="12" y="42" width="46" height="3"/></g>
    </svg>
    HOME THEATERS
  </div>

  <div class="abs service svc-camera">
    <svg width="60" height="46" viewBox="0 0 60 46" aria-hidden="true">
      <g fill="var(--blue)">
        <path d="M18 2 L58 16 L52 30 L12 16Z"/>
        <rect x="22" y="28" width="10" height="6" transform="rotate(20 27 31)"/>
        <rect x="6" y="30" width="20" height="5"/>
        <rect x="2" y="26" width="5" height="18"/>
      </g>
    </svg>
    SECURITY CAMERA<br>INSTALLATIONS
  </div>

  <footer class="abs footer"><span>Copyright © 2017, All rights reserved. <a>Privacy &amp; Policy</a></span></footer>
</body>
</html>
```